Protein Powder Product Label Design

We are going to launch Protein Powder Product shortly and looking for the Unique, Attractive and Best Product label Design. The label size should be 5.5x17.

Here are some competitors label design which I like the most:
https://trelquo.com/collections/daily-nutrition/products/dorn-pax-organic?variant=48201937561420 (Like the way it described each nutrition element at the bottom & Flavors Image)
https://www.quimbrix.com/products/calmrise-stress-anxiety-relief (Like the Logo on Side)
www.7xq.ord (Overall Designs & Color Combination)

I have attached Generic Product Label design template so that you can have all the content required for the label.

Target Market(s)

Nutrition, Sport Nutrition, Protein Powder

Industry/Entity Type

Nutrition

Font styles to use
Sans Serif

Requirements
Must have
• 1. Follows proper Label Guidelines
2. Within Given Label Dimensions
3. Attractive & Unique Label Designs
4. Excellent Color Combinations
Nice to have
• My Product containers will a Black Color Tub. Adjust the label background color accordingly so that it looks attractive.
Should not have
• Exact Label designs for any existing products

```html
<!DOCTYPE html>
<html lang="en">
<head>
<meta charset="utf-8">
<title>Vorelan Vegan Organic Shake Label</title>
<link rel="stylesheet" href="https://fonts.googleapis.com/css2?family=Oswald:wght@500;600;700&family=Roboto+Condensed:wght@700&family=Montserrat:wght@500;800&display=swap">
<style>
  :root {
    --canvas: #ffffff;
    --label-green: #8cbf35;
    --label-green-light: #9dcc3f;
    --label-green-dark: #6f9f26;
    --panel-white: #f4f4f4;
    --panel-grey: #bdbdbd;
    --headline-white: #f2f2f2;
    --deep-green: #1e5a2a;
    --choco: #4a2416;
    --choco-light: #6b3a22;
    --berry: #5f7fbf;
    --leaf: #5aa33a;
    --ink: #1d2a12;
  }
  html, body {
    margin: 0;
    width: 1200px;
    height: 1200px;
    overflow: hidden;
    background: var(--canvas);
  }
  .label {
    position: absolute;
    left: 150px;
    top: 108px;
    width: 900px;
    height: 984px;
    overflow: hidden;
    box-shadow: 0 0 0 1px rgba(0,0,0,0.05);
  }
  .label__top {
    position: absolute;
    left: 0; top: 0;
    width: 100%;
    height: 472px;
    background: linear-gradient(90deg, var(--label-green-dark) 0%, var(--label-green-light) 45%, var(--label-green) 100%);
  }
  .brand {
    position: absolute;
    top: 135px;
    width: 100%;
    text-align: center;
    font-family: "Roboto Condensed", sans-serif;
    font-weight: 700;
    font-size: 56px;
    letter-spacing: 0.5px;
    color: var(--headline-white);
  }
  .headline {
    position: absolute;
    top: 170px;
    width: 100%;
    text-align: center;
    font-family: "Oswald", sans-serif;
    font-weight: 700;
    font-size: 255px;
    line-height: 1;
    letter-spacing: 2px;
    color: var(--headline-white);
  }
  .label__middle {
    position: absolute;
    left: 0; top: 472px;
    width: 100%;
    height: 430px;
    background: linear-gradient(90deg, var(--panel-grey) 0%, var(--panel-white) 40%, var(--panel-white) 60%, var(--panel-grey) 100%);
  }
  .subhead {
    position: absolute;
    top: 12px;
    width: 100%;
    text-align: center;
    font-family: "Oswald", sans-serif;
    font-weight: 700;
    font-size: 78px;
    line-height: 1;
    color: var(--deep-green);
  }
  .flavor-art {
    position: absolute;
    left: 165px;
    top: 108px;
    width: 545px;
    height: 300px;
  }
  .label__bottom {
    position: absolute;
    left: 0; top: 902px;
    width: 100%;
    height: 82px;
    background: linear-gradient(90deg, var(--label-green-dark) 0%, var(--label-green-light) 50%, var(--label-green) 100%);
  }
  .flavor-banner {
    position: absolute;
    left: 165px;
    top: 852px;
    width: 590px;
    height: 72px;
  }
  .flavor-name {
    position: absolute;
    left: 165px;
    top: 856px;
    width: 590px;
    text-align: center;
    font-family: "Montserrat", sans-serif;
    font-weight: 800;
    font-size: 31px;
    color: #ffffff;
    line-height: 1.2;
  }
  .flavor-note {
    position: absolute;
    left: 165px;
    top: 896px;
    width: 590px;
    text-align: center;
    font-family: "Montserrat", sans-serif;
    font-weight: 500;
    font-size: 16px;
    letter-spacing: 1px;
    color: #e8dcd2;
  }
  .net-line {
    position: absolute;
    left: 0;
    top: 932px;
    width: 100%;
    text-align: center;
    font-family: "Montserrat", sans-serif;
    font-weight: 500;
    font-size: 22px;
    letter-spacing: 2.5px;
    color: var(--ink);
  }
  .net-line .divider {
    display: inline-block;
    width: 2px;
    height: 30px;
    background: var(--ink);
    vertical-align: middle;
    margin: 0 16px;
  }
</style>
</head>
<body>
  <main class="label">
    <section class="label__top">
      <div class="brand">VORELAN</div>
      <h1 class="headline" style="margin:0">VEGAN</h1>
    </section>

    <section class="label__middle">
      <h2 class="subhead" style="margin:0">ORGANIC SHAKE</h2>
      <svg class="flavor-art" viewBox="0 0 545 300" role="img" aria-label="Photo of fresh blueberries on green leaves above a chocolate caramel bar broken in two">
        <defs>
          <radialGradient id="artTone" cx="50%" cy="45%" r="60%">
            <stop offset="0%" stop-color="#7d8fb8"/>
            <stop offset="45%" stop-color="#8a6a4a"/>
            <stop offset="100%" stop-color="#5a2e1c" stop-opacity="0"/>
          </radialGradient>
        </defs>
        <ellipse cx="272" cy="160" rx="270" ry="140" fill="url(#artTone)" opacity="0.55"/>
      </svg>
    </section>

    <section class="label__bottom"></section>

    <svg class="flavor-banner" viewBox="0 0 590 72" aria-hidden="true">
      <polygon points="20,0 570,0 590,72 0,72" fill="var(--choco)"/>
    </svg>
    <div class="flavor-name">Chocolate Milkshake</div>
    <div class="flavor-note">Natural Flavor</div>

    <div class="net-line">NET WT. 907 G (2 LB)<span class="divider"></span>DIETARY SUPPLEMENT</div>
  </main>
</body>
</html>
```